Tea Shop - Drinks Menu - Vertical TV screen

Need a drinks menu design for a tea shop based in The Netherlands. Called Kettlova.
Currently we are trying to attract more customers for our Sip4Way and the idea came up to place 3 TV screen vertically in order to use 2 for the menu.
Website: http://kettlova-vosplein.nl/
Posible colour themes -
- Light green (same green as logo)
- Light brown
Dimensions of the screen -
- 40inch
- 905 mm Height
- 207 mm Width
Resolution of the menu must be 1920x1080 BUT VERTICAL
Needs to contain the following -
- Hot Sip4Way
- BLACK
- Delicate Earl Grey
- Bright Papaya Hug
- Plummy Orchard
- Spicy Chai
- Black Assam
- Duke of Nilgiri Hills
- Smokey Lapsang Suochong
- ( and many more teas, so leave space for aditional 5+)
- GREEN
- Sencha Lime-Ginger
- Sencha Forest Berries
- Sencha Orange Choco
- Happy Lotus
- Bancha
- Classic Gunpowder
- (space for aditional 4+)
- OOLONG
- Bullet Oolong
- Milky Oolong
- WHITE
- Bai Mu Tan
- HERBAL
- Kettlova's Dream
- Revitalising Kamille
- Pure Ginger
- Moon Blend
- Nana Mint
- Basil Strawberry
- FRUIT TEA
- Fruity Almond
- Berry Merry
- Pineapple Wink
- Spicy Pear
- Turkish Apple
- (space for aditional 2+)
- LATTÉ
- Spiced Chai
- Green Chai
- Vanille Chai
- Matcha
- Fresh Mint tea
- Iced Tea
- Peach
- Raspberry
- Lemon
- Mango
Divide this menu over 2 TV screens with the mentioned dimensions and use the font provided in the uploaded files (not mandatory if you think you have a bette idea).
Simple
Needs to attract people
Easy to adjust
Idea's are always welcome and appreciated
LOGO LINK : http://i66.pixbarn.com/7qkrzm4.png
(image too big to upload on here, sorry)
people whom drink TEA
Tv

```html
<!DOCTYPE html>
<html lang="en">
<head>
<meta charset="utf-8">
<title>Kettlova – Drinks Menu</title>
<link href="https://fonts.googleapis.com/css2?family=Ubuntu:wght@300;400&display=swap" rel="stylesheet">
<style>
  :root {
    --green: #a8c95c;
    --brown: #5b4d45;
    --ink: #4a3f38;
    --paper: #ffffff;
    --backdrop: #e9e9e9;
    --photo-light: #d9c8b4;
    --photo-dark: #8c6f55;
  }
  html, body {
    margin: 0;
    width: 1200px;
    height: 1200px;
    overflow: hidden;
    background: var(--backdrop);
  }
  .stage {
    position: relative;
    width: 1200px;
    height: 1200px;
  }
  .menu-screen {
    position: absolute;
    left: 263px;
    top: 0;
    width: 842px;
    height: 1500px;
    transform: scale(0.8);
    transform-origin: top left;
    background: var(--paper);
    overflow: hidden;
    font-family: "Ubuntu", sans-serif;
    color: var(--ink);
  }
  .decor {
    position: absolute;
    inset: 0;
  }
  .brand {
    position: absolute;
    left: 0;
    right: 0;
    top: 112px;
    text-align: center;
  }
  .brand-name {
    display: block;
    font-family: "Ubuntu", sans-serif;
    font-weight: 300;
    font-size: 104px;
    line-height: 1;
    color: var(--green);
    letter-spacing: 1px;
  }
  .brand-tagline {
    display: block;
    margin-top: 10px;
    font-weight: 300;
    font-size: 21px;
    letter-spacing: 1px;
    color: var(--brown);
  }
  .menu-column {
    position: absolute;
    top: 288px;
    margin: 0;
    padding: 0;
    list-style: none;
    font-weight: 300;
    font-size: 20px;
    line-height: 24.4px;
    white-space: nowrap;
  }
  .menu-column li::before { content: "- "; }
  .menu-column li.gap { height: 24.4px; }
  .menu-column li.gap::before { content: ""; }
  .col-black { left: 45px; }
  .col-herbal { left: 360px; }
  .col-specials {
    left: 645px;
    font-size: 22px;
    line-height: 26.3px;
  }
  .col-specials li.gap { height: 26.3px; }
</style>
</head>
<body>
<div class="stage">
  <section class="menu-screen">
    <svg class="decor" width="842" height="1500" viewBox="0 0 842 1500">
      <defs>
        <linearGradient id="photoTone" x1="0" y1="0" x2="1" y2="1">
          <stop offset="0" stop-color="var(--photo-light)"/>
          <stop offset="0.6" stop-color="#c9ab8a"/>
          <stop offset="1" stop-color="var(--photo-dark)"/>
        </linearGradient>
      </defs>
      <rect class="band-green" x="0" y="0" width="842" height="22" fill="var(--green)"/>
      <rect class="band-brown" x="0" y="22" width="842" height="26" fill="var(--brown)"/>
      <polygon class="band-brown" points="0,920 842,838 842,866 0,948" fill="var(--brown)"/>
      <polygon class="band-green" points="0,948 842,866 842,888 0,970" fill="var(--green)"/>
      <polygon class="hero-photo" role="img"
        aria-label="Photo of three branded takeaway tea cups, two hot and one iced with a pink straw, on a glass counter with red flowers"
        points="0,970 842,888 842,1500 0,1500" fill="url(#photoTone)"/>
    </svg>

    <header class="brand">
      <span class="brand-name">Kettlova</span>
      <span class="brand-tagline">Brewed From The Leaf</span>
    </header>

    <ul class="menu-column col-black">
      <li>Hot Sip4Way</li>
      <li>BLACK</li>
      <li>Delicate Earl Grey</li>
      <li>Bright Papaya Hug</li>
      <li>Plummy Orchard</li>
      <li>Spicy Chai</li>
      <li>Black Assam</li>
      <li>Duke of Nilgiri Hills</li>
      <li>Smokey Lapsang Suochong</li>
      <li>Sample 1</li>
      <li>Sample 2</li>
      <li>Sample 3</li>
      <li>Sample 4</li>
      <li class="gap"></li>
      <li>GREEN</li>
      <li>Sencha Lime-Ginger</li>
      <li>Sencha Forest Berries</li>
      <li>Sencha Orange Choco</li>
      <li>Happy Lotus</li>
      <li>Bancha</li>
      <li>Classic Gunpowder</li>
      <li>(space for aditional 4+)</li>
    </ul>

    <ul class="menu-column col-herbal">
      <li>OOLONG</li>
      <li>Bullet Oolong</li>
      <li>Milky Oolong</li>
      <li class="gap"></li>
      <li>HERBAL</li>
      <li>Kettlova's Dream</li>
      <li>Revitalising Kamille</li>
      <li>Pure Ginger</li>
      <li>Moon Blend</li>
      <li>Nana Mint</li>
      <li>Basil Strawberry</li>
      <li>(space for aditional 4+)</li>
      <li class="gap"></li>
      <li>FRUIT TEA</li>
      <li>Fruity Almond</li>
      <li>Berry Merry</li>
      <li>Pineapple Wink</li>
      <li>Spicy Pear</li>
      <li>Turkish Apple</li>
      <li>(space for aditional 2+)</li>
    </ul>

    <ul class="menu-column col-specials">
      <li>WHITE</li>
      <li>Bai Mu Tan</li>
      <li class="gap"></li>
      <li>LATTÉ</li>
      <li>Spiced Chai</li>
      <li>Green Chai</li>
      <li>Vanille Chai</li>
      <li>Matcha</li>
      <li class="gap"></li>
      <li>Fresh Mint tea</li>
      <li class="gap"></li>
      <li>Iced Tea</li>
      <li>Peach</li>
      <li>Raspberry</li>
      <li>Lemon</li>
      <li>Mango</li>
    </ul>
  </section>
</div>
</body>
</html>
```